International Legal Service Company needs Letterhead Design

Put my new Logo into Letterhead Design, using updated telephone number, e-mail address and website. Current letterhead and updated information which i want you to include my new letterhead attached herewith. Of course, my new Logo attached herein. Also, you can use slogan "Total Legal Outsourcing Solutions For Multinational Businesses"

It Company

```html
<!DOCTYPE html>
<html lang="en">
<head>
<meta charset="utf-8">
<title>Meridian Counsel Partners Inc — Letterhead</title>
<link rel="stylesheet" href="https://fonts.googleapis.com/css2?family=Montserrat:wght@600&family=Old+Standard+TT&display=swap">
<style>
  :root {
    --navy-dark: #1d3a72;
    --band-blue: #2b6aad;
    --brand-navy: #1f3e7c;
    --mark-blue: #2f6fc0;
    --ink: #111111;
    --paper: #ffffff;
  }
  html, body {
    margin: 0;
    padding: 0;
    overflow: hidden;
    background: var(--paper);
  }
  .letterhead {
    position: relative;
    width: 848px;
    height: 1200px;
    background: var(--paper);
    overflow: hidden;
  }
  .header-band-top {
    position: absolute;
    left: 0; top: 0;
    width: 848px; height: 17px;
    background: var(--navy-dark);
  }
  .header-band-main {
    position: absolute;
    left: 0; top: 21px;
    width: 848px; height: 40px;
    background: var(--band-blue);
  }
  .footer-band {
    position: absolute;
    left: 0; bottom: 0;
    width: 848px; height: 14px;
    background: var(--band-blue);
  }
  .brand {
    position: absolute;
    left: 27px; top: 86px;
    display: flex;
    align-items: center;
  }
  .brand-mark {
    width: 106px; height: 106px;
    border-radius: 50%;
    background: var(--mark-blue);
    flex: none;
  }
  .brand-name {
    margin: 0 0 0 27px;
    font-family: "Montserrat", sans-serif;
    font-weight: 600;
    font-size: 25px;
    line-height: 30px;
    color: var(--brand-navy);
  }
  .contact-block {
    position: absolute;
    right: 15px; top: 77px;
    margin: 0;
    font-family: "Old Standard TT", serif;
    font-style: normal;
    font-size: 14.5px;
    line-height: 19.7px;
    text-align: right;
    color: var(--ink);
  }
</style>
</head>
<body>
  <div class="letterhead">
    <div class="header-band-top"></div>
    <div class="header-band-main"></div>

    <div class="brand">
      <div class="brand-mark"></div>
      <p class="brand-name">Meridian Counsel<br>Partners Inc</p>
    </div>

    <address class="contact-block">
      1840 Harbor Crest Avenue<br>
      Suite 310<br>
      Fairview, MD 20912<br>
      Tel: 555-014-2298<br>
      Fax: 555-014-7731<br>
      E-Mail: office@meridiancounsel.example<br>
      Website: http://meridiancounsel.example.com
    </address>

    <div class="footer-band"></div>
  </div>
</body>
</html>
```